Business Card design for construction company

I would like a business card design for a construction company - ORD Builders. I have attached the ai logo file for use. I would like the card to be very smart and clean and incorporate only white and the two colours in the logo. I would like the card to have two sides. One side can just have the logo, the other with the relevant information.

Target Market(s)

Building and Construction Clients

Industry/Entity Type

Business

Contact Information for Business Card

Name: Tom Harcliffe
Company: ORD Builders Pty Limited
Address: 14 Mulberry Crescent Oakvale Heights 2093
Phone: 0432 517 208
Email: tomh@ordbuilders.example.au

Font styles to use
Serif
Sans Serif

Requirements
Must have
• Details noted above
• Logo as provided
• Colours as in logo
• Square edges
• A font that compliments the logo
Should not have
• Any colour other than white and those in logo
• Rounded edges

```html
<!DOCTYPE html>
<html lang="en">
<head>
<meta charset="utf-8">
<title>ORD Builders – Business Card</title>
<link rel="stylesheet" href="https://fonts.googleapis.com/css2?family=Michroma&family=Montserrat:wght@400;500&display=swap">
<style>
  :root {
    --bg: #e9eaeb;
    --card: #ffffff;
    --ink: #6d6e71;
    --ink-dark: #58595b;
    --accent: #29abe2;
    --block: #7a7b7d;
  }
  * { box-sizing: border-box; margin: 0; padding: 0; }
  html, body { width: 1200px; height: 864px; overflow: hidden; }
  body {
    background: var(--bg);
    display: flex;
    align-items: center;
    justify-content: center;
    gap: 40px;
  }
  .card {
    position: relative;
    width: 540px;
    height: 328px;
    background: var(--card);
    box-shadow: 0 6px 18px rgba(0,0,0,0.12);
    overflow: hidden;
  }
  .corner-block {
    position: absolute;
    width: 44px;
    height: 44px;
    background: var(--block);
  }
  .wordmark {
    position: absolute;
    font-family: "Michroma", sans-serif;
    color: var(--ink);
    letter-spacing: 0.08em;
    white-space: nowrap;
    display: flex;
    align-items: center;
    gap: 12px;
  }
  .wordmark-dot {
    width: 10px;
    height: 10px;
    background: var(--accent);
    display: inline-block;
  }

  /* Logo side */
  .card-logo .wordmark { top: 128px; left: 0; right: 0; justify-content: center; font-size: 30px; }
  .card-logo .block-left { left: 0; bottom: 70px; }
  .card-logo .block-right { right: 0; bottom: 0; }
  .legal-name {
    position: absolute;
    left: 0; right: 0;
    top: 210px;
    text-align: center;
    font-family: "Montserrat", sans-serif;
    font-size: 12px;
    color: var(--ink);
    letter-spacing: 0.04em;
  }

  /* Info side */
  .card-info .block-top { right: 0; top: 0; }
  .card-info .block-bottom { right: 0; bottom: 0; }
  .card-info .wordmark { top: 92px; right: 78px; font-size: 20px; }
  .rule {
    position: absolute;
    left: 0;
    top: 148px;
    width: 390px;
    height: 2px;
    background: var(--accent);
  }
  .person-name {
    position: absolute;
    right: 78px;
    top: 160px;
    font-family: "Michroma", sans-serif;
    font-size: 14px;
    letter-spacing: 0.12em;
    color: var(--ink-dark);
    text-transform: uppercase;
  }
  .contact-list {
    position: absolute;
    right: 58px;
    top: 204px;
    list-style: none;
    font-family: "Montserrat", sans-serif;
    font-size: 13px;
    color: var(--ink);
    text-align: right;
  }
  .contact-list li {
    display: flex;
    align-items: center;
    justify-content: flex-end;
    gap: 8px;
    height: 20px;
  }
  .contact-icon { width: 13px; height: 13px; flex: none; }
</style>
</head>
<body>

  <section class="card card-logo" aria-label="Business card, logo side">
    <div class="wordmark"><span class="wordmark-dot"></span>ORD Builders</div>
    <p class="legal-name">ORD Builders Pty Limited</p>
    <div class="corner-block block-left"></div>
    <div class="corner-block block-right"></div>
  </section>

  <section class="card card-info" aria-label="Business card, contact side">
    <div class="corner-block block-top"></div>
    <div class="corner-block block-bottom"></div>
    <div class="wordmark"><span class="wordmark-dot"></span>ORD Builders</div>
    <div class="rule"></div>
    <p class="person-name">Tom Harcliffe</p>
    <ul class="contact-list">
      <li>0432 517 208
        <svg class="contact-icon" viewBox="0 0 14 14" aria-hidden="true">
          <circle cx="7" cy="7" r="7" fill="var(--accent)"/>
          <path d="M4.6 3.6l1.2 1.6-.7.9c.4.9 1.1 1.6 2 2l.9-.7 1.6 1.2-.6 1.2c-2.6-.3-4.6-2.3-4.9-4.9z" fill="#fff"/>
        </svg>
      </li>
      <li>tomh@ordbuilders.example.au
        <svg class="contact-icon" viewBox="0 0 14 14" aria-hidden="true">
          <circle cx="7" cy="7" r="7" fill="var(--accent)"/>
          <rect x="3.6" y="4.6" width="6.8" height="4.8" fill="none" stroke="#fff" stroke-width="1"/>
          <path d="M3.6 4.8L7 7.4l3.4-2.6" fill="none" stroke="#fff" stroke-width="1"/>
        </svg>
      </li>
      <li>14 Mulberry Crescent Oakvale Heights 2093
        <svg class="contact-icon" viewBox="0 0 14 14" aria-hidden="true">
          <circle cx="7" cy="7" r="7" fill="var(--accent)"/>
          <path d="M7 3a2.4 2.4 0 0 0-2.4 2.4C4.6 7.2 7 10.6 7 10.6s2.4-3.4 2.4-5.2A2.4 2.4 0 0 0 7 3z" fill="#fff"/>
          <circle cx="7" cy="5.4" r="0.9" fill="var(--accent)"/>
        </svg>
      </li>
    </ul>
  </section>

</body>
</html>
```